Copper Meadow Packaging Design for RTE Beans

We need a product mock design that is aligned with our brand image. We need three SKUs. Black bean, Pinto bean, and Chickpeas. I've uploaded our brand logo here, Copper Meadow. I have also took a screenshot of the design elements that we would like to see. The packaging die line can be seen on the file "packaging sample". Please refer to the screenshots for packaging design directions.

```html
<!DOCTYPE html>
<html lang="en">
<head>
<meta charset="utf-8">
<title>Copper Meadow – Ready-to-Eat Beans Pouches</title>
<link href="https://fonts.googleapis.com/css2?family=Alfa+Slab+One&family=Special+Elite&family=Oswald:wght@500&display=swap" rel="stylesheet">
<style>
  :root {
    --bg: #e6e6e6;
    --rust: #9b5b3d;
    --olive: #6a6c2b;
    --cocoa: #6d4535;
    --parchment-light: #ecd39a;
    --parchment-dark: #d6b06a;
    --ink: #3a2a1d;
    --trim: #c9a46a;
    --badge: #d2ad78;
  }
  html, body { margin: 0; padding: 0; overflow: hidden; }
  body { width: 1200px; height: 960px; background: var(--bg); position: relative; }
  .pouch { position: absolute; width: 392px; height: 540px; }
  .pouch--black { left: 28px; top: 266px; z-index: 2; }
  .pouch--pinto { left: 398px; top: 142px; z-index: 1; }
  .pouch--chickpea { left: 768px; top: 266px; z-index: 2; }
  .pouch svg { display: block; overflow: visible; }
  .title { font-family: "Alfa Slab One", serif; fill: var(--ink); }
  .brand { font-family: "Alfa Slab One", serif; fill: var(--ink); }
  .tagline { font-family: "Special Elite", monospace; fill: var(--ink); }
  .netwt { font-family: "Oswald", sans-serif; font-weight: 500; fill: var(--ink); }
  .ready { font-family: "Oswald", sans-serif; font-weight: 500; fill: var(--trim); }
</style>
</head>
<body>

<div class="pouch pouch--black">
  <svg width="392" height="540" viewBox="0 0 392 540">
    <defs>
      <linearGradient id="parch" x1="0" y1="0" x2="0" y2="1">
        <stop offset="0" stop-color="var(--parchment-light)"/>
        <stop offset="1" stop-color="var(--parchment-dark)"/>
      </linearGradient>
      <linearGradient id="blackFood" x1="0" y1="0" x2="1" y2="1">
        <stop offset="0" stop-color="#4a3026"/>
        <stop offset="0.7" stop-color="#2c1a15"/>
        <stop offset="1" stop-color="#5b8a3a"/>
      </linearGradient>
    </defs>
    <rect class="pouch-body" width="392" height="540" fill="var(--rust)"/>
    <rect class="hang-hole" x="156" y="29" width="78" height="17" rx="8.5" fill="var(--bg)"/>
    <circle class="cert-badge" cx="75" cy="29" r="25" fill="none" stroke="var(--badge)" stroke-width="2"/>
    <text class="ready" x="322" y="24" font-size="14" text-anchor="middle">READY IN</text>
    <rect x="303" y="30" width="39" height="24" fill="none" stroke="var(--trim)" stroke-width="1.5"/>
    <text class="ready" x="316" y="48" font-size="11" text-anchor="middle">60</text>
    <line x1="20" y1="73" x2="372" y2="73" stroke="var(--trim)" stroke-width="0.8" opacity="0.7"/>
    <rect class="parchment" x="40" y="78" width="322" height="458" rx="10" fill="url(#parch)"/>
    <circle cx="196" cy="140" r="36" fill="none" stroke="var(--ink)" stroke-width="2"/>
    <text class="brand" x="196" y="210" font-size="20" text-anchor="middle">COPPER MEADOW</text>
    <text class="title" x="196" y="274" font-size="38" text-anchor="middle" textLength="300" lengthAdjust="spacingAndGlyphs">OUTLAW BLACK BEANS</text>
    <text class="tagline" x="196" y="299" font-size="11" text-anchor="middle" textLength="284" lengthAdjust="spacingAndGlyphs">SLOW SIMMERED WITH ONIONS, BELL PEPPERS AND SPICE</text>
    <rect x="96" y="311" width="212" height="194" fill="none" stroke="var(--trim)" stroke-width="3"/>
    <rect x="104" y="319" width="196" height="178" fill="url(#blackFood)" role="img" aria-label="Photo of simmered black beans with cilantro"/>
    <text class="netwt" x="196" y="528" font-size="17" text-anchor="middle">NET WT. 10 OZ (283G)</text>
  </svg>
</div>

<div class="pouch pouch--pinto">
  <svg width="392" height="540" viewBox="0 0 392 540">
    <defs>
      <linearGradient id="pintoFood" x1="0" y1="0" x2="1" y2="1">
        <stop offset="0" stop-color="#d89a78"/>
        <stop offset="1" stop-color="#b4653f"/>
      </linearGradient>
    </defs>
    <rect class="pouch-body" width="392" height="540" fill="var(--olive)"/>
    <rect class="hang-hole" x="156" y="29" width="78" height="17" rx="8.5" fill="var(--bg)"/>
    <circle class="cert-badge" cx="75" cy="29" r="25" fill="none" stroke="var(--badge)" stroke-width="2"/>
    <text class="ready" x="322" y="24" font-size="14" text-anchor="middle">READY IN</text>
    <rect x="303" y="30" width="39" height="24" fill="none" stroke="var(--trim)" stroke-width="1.5"/>
    <text class="ready" x="316" y="48" font-size="11" text-anchor="middle">60</text>
    <line x1="20" y1="73" x2="372" y2="73" stroke="var(--trim)" stroke-width="0.8" opacity="0.7"/>
    <rect class="parchment" x="40" y="78" width="322" height="458" rx="10" fill="url(#parch)"/>
    <circle cx="196" cy="140" r="36" fill="none" stroke="var(--ink)" stroke-width="2"/>
    <text class="brand" x="196" y="210" font-size="20" text-anchor="middle">COPPER MEADOW</text>
    <text class="title" x="196" y="274" font-size="38" text-anchor="middle" textLength="306" lengthAdjust="spacingAndGlyphs">SIDEKICK PINTO BEANS</text>
    <text class="tagline" x="196" y="299" font-size="11" text-anchor="middle" textLength="284" lengthAdjust="spacingAndGlyphs">SLOW SIMMERED WITH ONIONS, BELL PEPPERS AND SPICE</text>
    <rect x="96" y="311" width="212" height="194" fill="none" stroke="var(--trim)" stroke-width="3"/>
    <rect x="104" y="319" width="196" height="178" fill="url(#pintoFood)" role="img" aria-label="Photo of pinto beans topped with parsley"/>
    <text class="netwt" x="196" y="528" font-size="17" text-anchor="middle">NET WT. 10 OZ (283G)</text>
  </svg>
</div>

<div class="pouch pouch--chickpea">
  <svg width="392" height="540" viewBox="0 0 392 540">
    <defs>
      <linearGradient id="chickFood" x1="0" y1="0" x2="1" y2="1">
        <stop offset="0" stop-color="#f3e3b6"/>
        <stop offset="0.6" stop-color="#e9c37a"/>
        <stop offset="1" stop-color="#c9a27a"/>
      </linearGradient>
    </defs>
    <rect class="pouch-body" width="392" height="540" fill="var(--cocoa)"/>
    <rect class="hang-hole" x="156" y="29" width="78" height="17" rx="8.5" fill="var(--bg)"/>
    <circle class="cert-badge" cx="75" cy="29" r="25" fill="none" stroke="var(--badge)" stroke-width="2"/>
    <text class="ready" x="322" y="24" font-size="14" text-anchor="middle">READY IN</text>
    <rect x="303" y="30" width="39" height="24" fill="none" stroke="var(--trim)" stroke-width="1.5"/>
    <text class="ready" x="316" y="48" font-size="11" text-anchor="middle">60</text>
    <line x1="20" y1="73" x2="372" y2="73" stroke="var(--trim)" stroke-width="0.8" opacity="0.7"/>
    <rect class="parchment" x="40" y="78" width="322" height="458" rx="10" fill="url(#parch)"/>
    <circle cx="196" cy="140" r="36" fill="none" stroke="var(--ink)" stroke-width="2"/>
    <text class="brand" x="196" y="210" font-size="20" text-anchor="middle">COPPER MEADOW</text>
    <text class="title" x="196" y="274" font-size="38" text-anchor="middle" textLength="302" lengthAdjust="spacingAndGlyphs">JAILHOUSE CHICKPEAS</text>
    <text class="tagline" x="196" y="299" font-size="11" text-anchor="middle" textLength="284" lengthAdjust="spacingAndGlyphs">SLOW SIMMERED WITH ONIONS, BELL PEPPERS AND SPICE</text>
    <rect x="96" y="311" width="212" height="194" fill="none" stroke="var(--trim)" stroke-width="3"/>
    <rect x="104" y="319" width="196" height="178" fill="url(#chickFood)" role="img" aria-label="Photo of chickpeas with onions and peppers in a bowl"/>
    <text class="netwt" x="196" y="528" font-size="17" text-anchor="middle">NET WT. 10 OZ (283G)</text>
  </svg>
</div>

</body>
</html>
```